need 4 creative A frame (SANDWICH BOARD) designs concepts for dental office

need 4 creative A frame (SANDWICH BOARD) designs concepts
1 - targeting kids
2. targeting old age
3. targeting teens
4 targeting general public

website - www.pinecrestdental.ca

LINK for Measurements for sandwich board https://www.vordex.ca/KQ_4837/Steel-Clip-Rim-Folding-Board

i am attaching certain key ingredients ( rough sketch in uploaded files ) to be added on each design though not mandatory if the design is very creative

```html
<!DOCTYPE html>
<html lang="en">
<head>
<meta charset="utf-8">
<title>Pinecrest Dental – A-Frame Board Concepts</title>
<link href="https://fonts.googleapis.com/css2?family=Exo+2:wght@400;500;700;800&display=swap" rel="stylesheet">
<style>
  :root {
    --brand-blue: #3bb3d9;
    --brand-blue-dark: #2a9cc4;
    --ink-grey: #6d6e71;
    --board-bg: #f2f3f4;
    --page-bg: #ffffff;
    --white: #ffffff;
  }
  * { box-sizing: border-box; margin: 0; padding: 0; }
  html, body {
    width: 1200px; height: 571px; overflow: hidden;
    background: var(--page-bg);
    font-family: "Exo 2", sans-serif;
  }
  .board-row {
    position: absolute; left: 37px; top: 115px;
    display: flex; gap: 35px;
  }
  .board {
    position: relative; width: 255px; height: 340px;
    background: var(--board-bg);
    overflow: hidden;
    box-shadow: 0 0 0 1px #dcdfe2;
  }
  .board__photo {
    position: absolute; left: 0; top: 0; width: 100%; height: 215px;
  }
  .board__photo--general { background: linear-gradient(135deg, #e9c3a6 0%, #d9a88a 45%, #8fc3e0 100%); }
  .board__photo--teen    { background: linear-gradient(120deg, #eeeeee 0%, #d8b79c 50%, #b98a5c 75%, #ececec 100%); }
  .board__photo--kids    { background: linear-gradient(120deg, #3f7fb6 0%, #e3b796 45%, #5ea0cf 100%); }
  .board__photo--senior  { background: linear-gradient(120deg, #f1e9dd 0%, #d8c3a8 45%, #b7554f 60%, #e9eef2 100%); }
  .board__curve {
    position: absolute; left: 0; top: 0; width: 255px; height: 340px;
  }
  .badge {
    position: absolute; left: 184px; top: 92px;
    width: 50px; height: 50px; border-radius: 50%;
    background: var(--white); border: 3px solid var(--brand-blue);
    color: var(--brand-blue);
    display: flex; flex-direction: column; align-items: center; justify-content: center;
    line-height: 1;
  }
  .badge__hours { font-size: 15px; font-weight: 800; }
  .badge__label { font-size: 6px; font-weight: 700; letter-spacing: .5px; margin-top: 2px; }
  .brand-name {
    position: absolute; right: 18px; top: 160px;
    font-size: 21px; font-weight: 500; color: var(--ink-grey);
  }
  .cta-banner {
    position: absolute; left: 18px; top: 205px; width: 222px; height: 40px;
  }
  .cta-banner__text {
    position: absolute; left: 60px; top: 0; width: 162px; height: 40px;
    display: flex; align-items: center; justify-content: center;
    color: var(--white); font-size: 27px; font-weight: 800; letter-spacing: .5px;
  }
  .tagline {
    position: absolute; left: 0; right: 0; top: 257px; text-align: center;
    color: var(--ink-grey); font-size: 17px; font-weight: 400; letter-spacing: .3px;
  }
  .phone {
    position: absolute; left: 0; right: 0; top: 283px;
    display: flex; align-items: center; justify-content: center; gap: 7px;
    color: var(--brand-blue); font-size: 19px; font-weight: 700;
  }
</style>
</head>
<body>
<main class="board-row">

  <!-- General public -->
  <article class="board">
    <div class="board__photo board__photo--general" role="img" aria-label="Close-up photo of a patient's smile during a dental check-up with a gloved hand and mirror"></div>
    <svg class="board__curve" viewBox="0 0 255 340" aria-hidden="true">
      <path d="M0,200 C60,150 140,128 255,120 L255,340 L0,340 Z" fill="var(--board-bg)"/>
      <path d="M0,200 C60,150 140,128 255,120" fill="none" stroke="var(--brand-blue)" stroke-width="4"/>
    </svg>
    <div class="badge"><span class="badge__hours">24/7</span><span class="badge__label">SERVICE</span></div>
    <div class="brand-name">Pinecrest Dental</div>
    <div class="cta-banner">
      <svg width="222" height="40" viewBox="0 0 222 40" aria-hidden="true">
        <polyline points="22,2 4,20 22,38" fill="none" stroke="var(--brand-blue)" stroke-width="4"/>
        <polyline points="34,2 16,20 34,38" fill="none" stroke="var(--brand-blue)" stroke-width="4"/>
        <polygon points="60,0 222,0 222,40 60,40 42,20" fill="var(--brand-blue)"/>
      </svg>
      <span class="cta-banner__text">WE’RE IN</span>
    </div>
    <p class="tagline">Accepting New Patients</p>
    <p class="phone">
      <svg width="20" height="20" viewBox="0 0 20 20" aria-hidden="true"><circle cx="10" cy="10" r="8.5" fill="none" stroke="var(--brand-blue)" stroke-width="1.6"/><path d="M7 5.5l1.6 2.4-1 1.1c.6 1.3 1.5 2.2 2.8 2.8l1.1-1 2.4 1.6-.8 1.6c-3.5-.3-6.6-3.4-7-7z" fill="var(--brand-blue)"/></svg>
      (555) 014-2738
    </p>
  </article>

  <!-- Teens -->
  <article class="board">
    <div class="board__photo board__photo--teen" role="img" aria-label="Photo of a smiling teenager with braces pointing at her smile"></div>
    <svg class="board__curve" viewBox="0 0 255 340" aria-hidden="true">
      <path d="M0,200 C60,150 140,128 255,120 L255,340 L0,340 Z" fill="var(--board-bg)"/>
      <path d="M0,200 C60,150 140,128 255,120" fill="none" stroke="var(--brand-blue)" stroke-width="4"/>
    </svg>
    <div class="badge"><span class="badge__hours">24/7</span><span class="badge__label">SERVICE</span></div>
    <div class="brand-name">Pinecrest Dental</div>
    <div class="cta-banner">
      <svg width="222" height="40" viewBox="0 0 222 40" aria-hidden="true">
        <polyline points="22,2 4,20 22,38" fill="none" stroke="var(--brand-blue)" stroke-width="4"/>
        <polyline points="34,2 16,20 34,38" fill="none" stroke="var(--brand-blue)" stroke-width="4"/>
        <polygon points="60,0 222,0 222,40 60,40 42,20" fill="var(--brand-blue)"/>
      </svg>
      <span class="cta-banner__text">WE’RE IN</span>
    </div>
    <p class="tagline">Accepting New Patients</p>
    <p class="phone">
      <svg width="20" height="20" viewBox="0 0 20 20" aria-hidden="true"><circle cx="10" cy="10" r="8.5" fill="none" stroke="var(--brand-blue)" stroke-width="1.6"/><path d="M7 5.5l1.6 2.4-1 1.1c.6 1.3 1.5 2.2 2.8 2.8l1.1-1 2.4 1.6-.8 1.6c-3.5-.3-6.6-3.4-7-7z" fill="var(--brand-blue)"/></svg>
      (555) 014-2738
    </p>
  </article>

  <!-- Kids -->
  <article class="board">
    <div class="board__photo board__photo--kids" role="img" aria-label="Photo of a happy young boy in the dental chair during a check-up"></div>
    <svg class="board__curve" viewBox="0 0 255 340" aria-hidden="true">
      <path d="M0,200 C60,150 140,128 255,120 L255,340 L0,340 Z" fill="var(--board-bg)"/>
      <path d="M0,200 C60,150 140,128 255,120" fill="none" stroke="var(--brand-blue)" stroke-width="4"/>
    </svg>
    <div class="badge"><span class="badge__hours">24/7</span><span class="badge__label">SERVICE</span></div>
    <div class="brand-name">Pinecrest Dental</div>
    <div class="cta-banner">
      <svg width="222" height="40" viewBox="0 0 222 40" aria-hidden="true">
        <polyline points="22,2 4,20 22,38" fill="none" stroke="var(--brand-blue)" stroke-width="4"/>
        <polyline points="34,2 16,20 34,38" fill="none" stroke="var(--brand-blue)" stroke-width="4"/>
        <polygon points="60,0 222,0 222,40 60,40 42,20" fill="var(--brand-blue)"/>
      </svg>
      <span class="cta-banner__text">WE’RE IN</span>
    </div>
    <p class="tagline">Accepting New Patients</p>
    <p class="phone">
      <svg width="20" height="20" viewBox="0 0 20 20" aria-hidden="true"><circle cx="10" cy="10" r="8.5" fill="none" stroke="var(--brand-blue)" stroke-width="1.6"/><path d="M7 5.5l1.6 2.4-1 1.1c.6 1.3 1.5 2.2 2.8 2.8l1.1-1 2.4 1.6-.8 1.6c-3.5-.3-6.6-3.4-7-7z" fill="var(--brand-blue)"/></svg>
      (555) 014-2738
    </p>
  </article>

  <!-- Seniors -->
  <article class="board">
    <div class="board__photo board__photo--senior" role="img" aria-label="Photo of an older patient being treated by two dental staff beside an X-ray screen"></div>
    <svg class="board__curve" viewBox="0 0 255 340" aria-hidden="true">
      <path d="M0,200 C60,150 140,128 255,120 L255,340 L0,340 Z" fill="var(--board-bg)"/>
      <path d="M0,200 C60,150 140,128 255,120" fill="none" stroke="var(--brand-blue)" stroke-width="4"/>
    </svg>
    <div class="badge"><span class="badge__hours">24/7</span><span class="badge__label">SERVICE</span></div>
    <div class="brand-name">Pinecrest Dental</div>
    <div class="cta-banner">
      <svg width="222" height="40" viewBox="0 0 222 40" aria-hidden="true">
        <polyline points="22,2 4,20 22,38" fill="none" stroke="var(--brand-blue)" stroke-width="4"/>
        <polyline points="34,2 16,20 34,38" fill="none" stroke="var(--brand-blue)" stroke-width="4"/>
        <polygon points="60,0 222,0 222,40 60,40 42,20" fill="var(--brand-blue)"/>
      </svg>
      <span class="cta-banner__text">WE’RE IN</span>
    </div>
    <p class="tagline">Accepting New Patients</p>
    <p class="phone">
      <svg width="20" height="20" viewBox="0 0 20 20" aria-hidden="true"><circle cx="10" cy="10" r="8.5" fill="none" stroke="var(--brand-blue)" stroke-width="1.6"/><path d="M7 5.5l1.6 2.4-1 1.1c.6 1.3 1.5 2.2 2.8 2.8l1.1-1 2.4 1.6-.8 1.6c-3.5-.3-6.6-3.4-7-7z" fill="var(--brand-blue)"/></svg>
      (555) 014-2738
    </p>
  </article>

</main>
</body>
</html>
```